3D Printing Website redesign

We are in the process of redesigning our website. Attached is an image of one of the proposed pages - "The Quotewheel". The idea with this page is that site visitors can get an indicative estimate of the cost of 3D Printing based on some provided metrics. When the user alters the metrics the price changes accordingly. We are looking for a design to support this page that will also be used across our site.

Industry/Entity Type

Printing

```html
<!DOCTYPE html>
<html lang="en">
<head>
<meta charset="utf-8">
<title>Layerworks Studio</title>
<link href="https://fonts.googleapis.com/css2?family=Lato:wght@300;400;700&display=swap" rel="stylesheet">
<style>
:root{
  --topbar:#3c80c6;
  --topbar-dark:#2d5d9c;
  --navy:#2f3c86;
  --navy-deep:#2e3d7c;
  --circle:#3f51a3;
  --circle-edge:#2f3f8a;
  --hero-a:#2c3d94;
  --hero-b:#4a5fb0;
  --page:#efefef;
  --band:#d9dce9;
  --grey-text:#777;
  --body-text:#444;
  --white:#fff;
}
*{margin:0;padding:0;box-sizing:border-box}
html,body{width:993px;height:1200px;overflow:hidden;background:var(--page);font-family:"Lato",sans-serif}
.page{position:relative;width:993px;height:1200px}
.abs{position:absolute}

.topbar{left:0;top:0;width:993px;height:40px;background:var(--topbar)}
.home-btn{left:0;top:0;width:40px;height:40px;background:var(--topbar-dark)}
.contact{left:160px;top:0;height:40px;display:flex;align-items:center;gap:8px;color:var(--white);font-size:13px}
.contact span{white-space:nowrap}
.auth{top:4px;height:32px;border:1px solid var(--white);color:var(--white);font-size:13px;display:flex;align-items:center;justify-content:center}
.login{left:701px;width:71px}
.register{left:776px;width:71px}
.tool{top:0;width:39px;height:40px;background:var(--topbar-dark)}
.menu-btn{left:915px}.search-btn{left:954px;background:#3366a8}

.header{left:0;top:40px;width:993px;height:60px;background:var(--white)}
.brand{left:153px;top:49px;display:flex;align-items:center;gap:8px}
.brand-mark{width:48px;height:48px;border-radius:50%;background:#5c6b8c}
.brand-name{font-size:19px;font-weight:700;color:var(--navy)}
.nav{left:365px;top:66px;display:flex;font-size:9.5px;color:#444;text-transform:uppercase}
.nav span{padding:0 6px;border-left:1px solid #bbb;line-height:12px}
.nav span:first-child{border:0;padding-left:0;color:var(--topbar)}

.hero{left:0;top:100px;width:993px;height:334px;background:linear-gradient(100deg,var(--hero-a),var(--hero-b) 55%,#5a6fb8)}
.hero-photo{left:585px;top:100px;width:408px;height:334px;background:linear-gradient(180deg,#7d8dc4,#4b5a9c 60%,#2f3a73)}
.hero-arch{left:0;top:100px}
.hero-kicker{left:149px;top:172px;font-size:24px;font-weight:300;color:var(--white)}
.hero-title{left:147px;top:194px;font-size:70px;font-weight:700;color:var(--white);line-height:74px}
.hero-sub{left:147px;top:258px;font-size:42px;font-weight:300;color:var(--white);line-height:46px}
.hero-lead{left:149px;top:326px;width:360px;font-size:16px;font-weight:300;color:var(--white);line-height:19px}
.dots{left:147px;top:386px;display:flex;gap:9px}
.dots i{width:20px;height:20px;border-radius:50%;background:var(--white)}
.dots i.active{background:linear-gradient(#dfe6f5,#7f94cc)}

.intro{left:0;top:458px;width:993px;text-align:center}
.intro h1{font-size:24px;font-weight:300;color:var(--navy-deep);line-height:29px}
.intro p{margin-top:14px;font-size:16px;font-weight:300;color:var(--grey-text);line-height:19px}
.offer-title{left:0;top:594px;width:993px;text-align:center;font-size:23px;font-weight:300;color:var(--navy-deep)}
.step{top:648px;width:122px;height:122px;border-radius:50%;background:var(--circle-edge);color:var(--white);text-align:center;display:flex;flex-direction:column;justify-content:center;font-size:16px}
.step::before{content:"";position:absolute;left:6px;top:4px;width:110px;height:110px;border-radius:50%;background:linear-gradient(var(--circle),#4a5cab)}
.step b,.step span{position:relative}
.step span{font-weight:300}
.arrow{top:698px;width:0;height:0;border-top:10px solid transparent;border-bottom:10px solid transparent;border-left:13px solid #8c96c4}

.band{left:0;top:792px;width:993px;height:211px;background:var(--band)}
.col{top:816px;width:195px}
.col h2{font-size:18px;font-weight:400;color:var(--navy-deep);margin-bottom:12px}
.col p{font-size:11.5px;font-weight:300;color:var(--body-text);line-height:14px}
.cta{top:933px;width:189px;height:44px;border:1px solid var(--navy-deep);display:flex;align-items:center;justify-content:center;font-size:12px;color:var(--navy-deep);text-transform:uppercase}

.links{top:1026px;font-size:9px;color:#444;line-height:13px}
.links b{color:var(--navy-deep);font-weight:700;display:block}
.links .gap{height:13px}
.news-title{left:566px;top:1023px;font-size:19px;font-weight:700;color:var(--navy-deep)}
.news-sub{left:566px;top:1046px;font-size:18px;font-weight:300;color:#555}
.news-field{left:565px;top:1078px;width:255px;height:30px;background:var(--white);border:1px solid #ccc;font-size:10px;color:#999;padding:8px 14px;letter-spacing:.3px}
.follow{left:566px;top:1117px;display:flex;align-items:center;gap:4px;font-size:12px;font-weight:700;color:#444}
.follow i{width:20px;height:20px;border-radius:50%;background:var(--navy)}
.follow i+i{background:#2aa3dc}

.footer{left:0;top:1160px;width:993px;height:40px;background:var(--navy-deep);color:var(--white);font-size:9px;display:flex;align-items:center;justify-content:center;gap:10px}
</style>
</head>
<body>
<div class="page">
  <div class="abs topbar"></div>
  <div class="abs home-btn">
    <svg width="40" height="40" viewBox="0 0 40 40"><path d="M10 20 L20 11 L30 20 M13 18 V29 H18 V23 H22 V29 H27 V18" fill="#fff" stroke="#fff" stroke-width="1.5" stroke-linejoin="round"/></svg>
  </div>
  <div class="abs contact">
    <svg width="18" height="18" viewBox="0 0 18 18"><path d="M4 2 L7 2 L8 6 L6 7.5 Q7.5 10.5 10.5 12 L12 10 L16 11 L16 14 Q9 16 4 9 Q2 5 4 2Z" fill="#fff"/></svg>
    <span>61 2 5550 1234 &nbsp;| &nbsp;0400 555 012 &nbsp;| &nbsp;UAN &nbsp;111-000-555 &nbsp;| &nbsp;Australia</span>
  </div>
  <div class="abs auth login">LOG IN</div>
  <div class="abs auth register">REGISTER</div>
  <div class="abs tool menu-btn">
    <svg width="39" height="40" viewBox="0 0 39 40"><rect x="10" y="13" width="19" height="3" fill="#fff"/><rect x="10" y="19" width="19" height="3" fill="#fff"/><rect x="10" y="25" width="19" height="3" fill="#fff"/></svg>
  </div>
  <div class="abs tool search-btn">
    <svg width="39" height="40" viewBox="0 0 39 40"><circle cx="22" cy="17" r="6" fill="none" stroke="#fff" stroke-width="2.5"/><line x1="17.5" y1="21.5" x2="11" y2="28" stroke="#fff" stroke-width="3.5" stroke-linecap="round"/></svg>
  </div>

  <div class="abs header"></div>
  <div class="abs brand"><span class="brand-mark"></span><span class="brand-name">Layerworks Studio</span></div>
  <nav class="abs nav">
    <span>Shop</span><span>What we do</span><span>The Quotewheel</span><span>Materials</span><span>Gallery</span><span>DIY</span><span>Training</span><span>About us</span><span>Blog</span>
  </nav>

  <section class="abs hero"></section>
  <div class="abs hero-photo" role="img" aria-label="Night-lit architectural model of a multi-storey apartment building with cars"></div>
  <svg class="abs hero-arch" width="993" height="60" viewBox="0 0 993 60"><path d="M0 0 H993 V46 Q500 -30 0 48 Z" fill="#fff"/></svg>
  <div class="abs hero-kicker">ARCHITECTURAL MODELS</div>
  <div class="abs hero-title">3D PRINTS</div>
  <div class="abs hero-sub">DEVELOPER</div>
  <p class="abs hero-lead">One stop shop for everyting 3D Printing located in the trendy Rocks area of Sydney</p>
  <div class="abs dots"><i></i><i class="active"></i><i></i></div>

  <section class="abs intro">
    <h1>Australia’s 1st 3D Printing Shop opens in The Rocks, Sydney<br>3D Printing has arrived in Australia.</h1>
    <p>At the Studio you can see 3D Printers in Action, do training, shop and get all your designs<br>brought to life using our bank of printers. So why not head down?</p>
  </section>
  <h2 class="abs offer-title">What we offer</h2>
  <div class="abs step" style="left:148px"><b>3D</b><span>SCANNING</span></div>
  <div class="abs arrow" style="left:270px"></div>
  <div class="abs step" style="left:292px"><b>3D</b><span>DESIGN</span></div>
  <div class="abs arrow" style="left:414px"></div>
  <div class="abs step" style="left:437px"><b>PRINT</b><span>READINESS</span></div>
  <div class="abs arrow" style="left:559px"></div>
  <div class="abs step" style="left:582px"><b>3D</b><span>PRINTING</span></div>
  <div class="abs arrow" style="left:704px"></div>
  <div class="abs step" style="left:725px"><b>FINISHING</b></div>

  <section class="abs band"></section>
  <div class="abs col" style="left:149px"><h2>3D Printing on Demand</h2><p>Need a thing 3D printed? Need help with 3D modelling an idea? the studio is here to help. Simply let us know what you need or head into the shop to find out what is possible</p></div>
  <div class="abs col" style="left:396px"><h2>Training Classes</h2><p>Newbie to 3D Printing or are you an experienced printer? We offer a range of training classes at our Sydney based studio, we also host the Harbour Makers meetup.</p></div>
  <div class="abs col" style="left:641px"><h2>3D Printers &amp; Materials</h2><p>Looking to get yourself a 3D Printer for your home? We have a wide range of the latest 3D Printers and consumables</p></div>
  <div class="abs cta" style="left:147px">Get a quote</div>
  <div class="abs cta" style="left:396px">Find a class</div>
  <div class="abs cta" style="left:642px">Find a printer</div>

  <div class="abs links" style="left:149px"><b>Printing</b>Quote<br>Technologies<div class="gap"></div><b>Printers</b>Machines for sale<br>Machines to rent<br>Servicing<br>Buy Materials</div>
  <div class="abs links" style="left:270px"><b>Materials</b>Overview<br>Plastic<br>Powder<br>High-Detail Resin<br>Nylon<br>Wood<br>Rubber</div>
  <div class="abs links" style="left:398px"><b>Training</b>Harbour Makers<br>Meetup<br>Studio Workshops<div class="gap"></div><b>Franchise</b>Franchise Opportunity</div>
  <div class="abs news-title">Newsletter</div>
  <div class="abs news-sub">Want to receive our Newsletter?</div>
  <div class="abs news-field">ENTER YOUR EMAIL
    <svg style="position:absolute;right:10px;top:5px" width="38" height="20" viewBox="0 0 38 20"><line x1="0" y1="5" x2="8" y2="5" stroke="#333"/><line x1="3" y1="10" x2="10" y2="10" stroke="#333"/><rect x="13" y="3" width="22" height="14" fill="none" stroke="#333" stroke-width="1.5"/><path d="M13 3 L24 11 L35 3" fill="none" stroke="#333" stroke-width="1.5"/></svg>
  </div>
  <div class="abs follow">Follow Us On&nbsp;<i></i><i></i></div>

  <footer class="abs footer"><span>COPYRIGHT © 2014 LAYERWORKS STUDIO</span><span>|</span><span>ALL RIGHTS RESERVED</span></footer>
</div>
</body>
</html>
```